New Innovative Counselling and psychotherapy Service needs Business Card design

Keep it simple and professional. On one side, just company name and logo (perhaps in all blue) and maybe a tag line.

On other side (all white) my name and Qualifications in centre

Industry/Entity Type

Health And Wellness

Contact Information for Business Card

Derek Hollis
Counsellor & Psychotherapist
BSc (Psychol.), BA, Dip. (Couns. & Psych.), PG.Cert (CBT), MGVrA, NWTF

I will also require Mobile no, Email and web site address of which I'll pass on to final designer.

Font styles to use
Sans Serif

Requirements
Must have
• My Logo Only and please use the colours in logo that is in it.
Should not have
• Any other images

```html
<!DOCTYPE html>
<html lang="en">
<head>
<meta charset="utf-8">
<title>Kindred Lane – Business Card</title>
<link rel="stylesheet" href="https://fonts.googleapis.com/css2?family=Lato:wght@300;400&family=Cormorant+Garamond:ital,wght@1,500&display=swap">
<style>
  :root {
    --page-bg: #9b9b9b;
    --card-light: #f7f7f7;
    --card-dark: #3b3b3b;
    --ink: #2b2b2b;
    --ink-soft: #333333;
    --brand-blue: #3aaee8;
    --brand-green: #8cc63f;
    --faint-blue: #e6f1f8;
    --faint-dark: #444444;
    --on-dark: #e8e8e8;
  }
  * { margin: 0; padding: 0; box-sizing: border-box; }
  html, body { width: 1200px; height: 802px; overflow: hidden; }
  body {
    position: relative;
    background: var(--page-bg);
    font-family: "Lato", sans-serif;
    color: var(--ink);
  }
  .card {
    position: absolute;
    top: 274px;
    width: 443px;
    height: 264px;
    overflow: hidden;
    box-shadow: 2px 3px 6px rgba(0,0,0,0.35);
  }
  .card--front { left: 136px; background: var(--card-light); }
  .card--back { left: 624px; background: var(--card-dark); }

  .card__accent {
    position: absolute;
    border-radius: 50%;
  }
  .card--front .card__accent {
    left: 211px; top: 0; width: 232px; height: 232px;
    background: var(--faint-blue);
  }
  .card--back .card__accent {
    left: 2px; top: 0; width: 226px; height: 226px;
    background: var(--faint-dark);
  }

  .wordmark {
    position: absolute;
    font-family: "Lato", sans-serif;
    font-weight: 300;
    white-space: nowrap;
  }
  .card--front .wordmark {
    left: 22px; top: 38px;
    font-size: 37px;
    color: var(--ink);
    letter-spacing: 0.2px;
  }
  .card--back .brand {
    position: absolute;
    left: 113px; top: 107px;
    display: flex; align-items: center; gap: 12px;
  }
  .brand__dot {
    width: 42px; height: 42px; border-radius: 50%;
    background: var(--brand-blue);
  }
  .card--back .wordmark {
    position: static;
    font-size: 23px;
    color: var(--on-dark);
  }

  .person {
    position: absolute;
    left: 25px; top: 119px;
  }
  .person__name {
    font-size: 17px;
    font-weight: 400;
    letter-spacing: 0.3px;
    line-height: 1.2;
  }
  .person__first { color: var(--brand-blue); }
  .person__last { color: var(--brand-green); }
  .person__role, .person__quals {
    font-size: 12.5px;
    line-height: 16px;
    color: var(--ink-soft);
  }
  .contact {
    position: absolute;
    left: 25px; top: 199px;
    list-style: none;
    font-size: 12.5px;
    line-height: 16px;
    color: var(--ink);
  }
  .contact li { display: flex; align-items: center; gap: 5px; }
  .contact svg { width: 10px; height: 10px; flex: none; }

  .tagline {
    position: absolute;
    left: 0; right: 0; top: 194px;
    text-align: center;
    font-family: "Cormorant Garamond", serif;
    font-style: italic;
    font-weight: 500;
    font-size: 17px;
    line-height: 20px;
    color: var(--on-dark);
  }
</style>
</head>
<body>
  <section class="card card--front" aria-label="Business card, contact side">
    <div class="card__accent" aria-hidden="true"></div>
    <div class="wordmark">Kindred Lane</div>
    <div class="person">
      <div class="person__name"><span class="person__first">DEREK</span> <span class="person__last">HOLLIS</span></div>
      <div class="person__role">Counsellor &amp; Psychotherapist</div>
      <div class="person__quals">BSc (Psychol.), BA, Dip. (Couns. &amp; Psych.),<br>PG.Cert (CBT), MGVrA, NWTF</div>
    </div>
    <ul class="contact">
      <li>
        <svg viewBox="0 0 10 10" aria-hidden="true"><path d="M1 3.5 C1 2 2.5 1.5 5 1.5 S9 2 9 3.5 L7.5 4 L7 3 H3 L2.5 4 Z M2.5 5 H7.5 L8.5 8.5 H1.5 Z" fill="#3aaee8"/></svg>
        087 5290 416
      </li>
      <li>
        <svg viewBox="0 0 10 10" aria-hidden="true"><rect x="0.5" y="2" width="9" height="6.5" fill="#3aaee8"/><path d="M0.5 2 L5 5.8 L9.5 2" stroke="#fff" stroke-width="0.9" fill="none"/></svg>
        info@kindredlane.com
      </li>
      <li>
        <svg viewBox="0 0 10 10" aria-hidden="true"><circle cx="5" cy="5" r="4.5" fill="#3aaee8"/><path d="M3 3.5 Q5 2.5 6 4 Q5 6 6.5 7.5" stroke="#8cc63f" stroke-width="1.3" fill="none"/></svg>
        www.kindredlane.com
      </li>
    </ul>
  </section>

  <section class="card card--back" aria-label="Business card, brand side">
    <div class="card__accent" aria-hidden="true"></div>
    <div class="brand">
      <div class="brand__dot" aria-hidden="true"></div>
      <div class="wordmark">Kindred Lane</div>
    </div>
    <p class="tagline">Caring For Your Psychological<br>Well-Being Is Our Top Priority</p>
  </section>
</body>
</html>
```